Lucia''s Blue Pantry - blog, shop and recipes - web design

I will be using wordpress and need a website developed to allow me to do daily blogs of recipes and food comments, an index of my recipes and a shop where people can buy my products including food (pasta and sauce kits, cannoli, biscotti) and my upcoming unique aprons for example. I have already selected a logo which I have copied the files to this brief.

The feel of the entire site should be modern but classic and clean. The main colour of the site should be red and the same red as my logo. I will eventually include a photo of myself and I would like the home page to read; Lucia Marbetto in (insert logo) Lucia's Blue Pantry

Home page:
1. Needs to allow me to write daily updates on what I'm cooking or eating etc. and include upload of photos of food.
2. Needs an index/link to recipes broken down into: Antipasto, Starters, Sides, Mains, Desserts, Thermomix Recipes.
3. Needs to have the following links: Home, Recipes, About, Contact us, Shop, Events, Travel. All of these links will need separate pages with links to other pages etc.
4. There should also be icons for links to email, facebook, pinterest, and twitter. It should say Follow Me! or Connect with Me!

Recipe pages:
1. Need to have a template to enter recipes and photos.

About Page:
1. Will have my story.

Contact us page:
1. Contact details to be provided.

Events
1. This will contain news and events like cooking classes that I will be holding.

Shop:
1. This page will need to allow items to be purchased and paid for via paypal.

Travel:
1. This page will include photos and information on food related places I have travelled.

Please do not hesitate to contact me if you need any further information.

Requirements
Should not have
• This is NOT a restaurant or cafe and therefore should not include links or headers such as business hours or menu.

```html
<!DOCTYPE html>
<html lang="en">
<head>
<meta charset="utf-8">
<title>Lucia's Blue Pantry</title>
<link href="https://fonts.googleapis.com/css2?family=Open+Sans:wght@400;600&family=Actor&family=Great+Vibes&display=swap" rel="stylesheet">
<style>
  :root {
    --cream: #fdfcf0;
    --red: #d0121b;
    --red-dark: #ad0000;
    --red-light: #dc0a0a;
    --gold-dark: #c48f0b;
    --card-border: #e6c597;
    --grey-text: #7a7a7a;
    --frame: #4a3a30;
  }
  * { box-sizing: border-box; margin: 0; padding: 0; }
  html, body { width: 1200px; height: 1026px; overflow: hidden; }
  body {
    position: relative;
    background: var(--cream);
    font-family: 'Open Sans', Arial, sans-serif;
  }
  .site-header { position: absolute; left: 0; top: 0; width: 1200px; height: 167px; }
  .brand { position: absolute; left: 112px; top: 52px; display: flex; align-items: center; gap: 16px; }
  .brand-mark { width: 54px; height: 54px; border-radius: 50%; background: var(--red); }
  .brand-name { font-weight: 400; font-size: 34px; color: var(--red); letter-spacing: 1px; }
  .follow { position: absolute; top: 66px; left: 905px; display: flex; gap: 8px; }
  .follow-icon { width: 44px; height: 44px; border-radius: 50%; border: 2px solid #fff; box-shadow: 0 0 0 1px rgba(0,0,0,.25); }
  .follow-icon.blue-dark { background: #2f5fa5; }
  .follow-icon.blue-light { background: #2aa3e0; }
  .follow-icon.red { background: #c8182a; }
  .follow-icon.orange { background: #f4a324; display: flex; align-items: center; justify-content: center; }

  .main-nav {
    position: absolute; left: 0; top: 167px; width: 1200px; height: 56px;
    background: linear-gradient(var(--red-light), var(--red-dark));
  }
  .nav-item {
    position: absolute; top: 0; height: 56px; line-height: 56px;
    color: #fff; font-size: 17px; transform: translateX(-50%); white-space: nowrap;
  }
  .nav-sep { position: absolute; top: 0; width: 1px; height: 56px; background: rgba(255,255,255,.35); }

  .hero {
    position: absolute; left: 93px; top: 236px; width: 1053px; height: 310px;
    border: 2px solid var(--frame); overflow: hidden;
  }
  .hero-photo {
    position: absolute; inset: 0;
    background: linear-gradient(100deg, #f5efe9 0%, #dcb9a0 18%, #f3e6dc 32%, #ece7de 45%, #5b5048 52%, #f2eee8 58%, #f0a866 70%, #f6d38c 82%, #9bb05a 100%);
  }
  .hero-title {
    position: absolute; left: 381px; top: 206px;
    font-family: 'Great Vibes', cursive; font-weight: 400; font-size: 60px; color: var(--red);
    text-shadow: 0 0 3px #fff, 0 0 3px #fff;
    white-space: nowrap;
  }

  .section-title {
    position: absolute; left: 113px; top: 568px;
    font-family: 'Great Vibes', cursive; font-weight: 400; font-size: 42px; color: var(--red);
  }
  .product {
    position: absolute; top: 637px; width: 229px; height: 370px;
    border: 1px solid var(--card-border); text-align: center;
  }
  .product-photo {
    position: absolute; left: 12px; top: 14px; width: 204px; height: 181px;
    border: 1px solid #bbb;
  }
  .product-name {
    position: absolute; left: 0; right: 0; top: 203px;
    font-family: 'Actor', Arial, sans-serif; font-weight: 400; font-size: 18px; color: var(--red);
  }
  .product-text {
    position: absolute; left: 12px; right: 12px; top: 233px;
    font-size: 13.5px; line-height: 16.5px; color: var(--grey-text);
  }
  .product-price { position: absolute; left: 0; right: 0; top: 291px; font-size: 18px; color: var(--red); }
  .btn {
    position: absolute; top: 322px; width: 79px; height: 35px; line-height: 33px;
    font-size: 14px; color: #fff; border-radius: 3px;
  }
  .btn-buy { left: 36px; background: linear-gradient(#ee1c1c, #c40000); border: 1px solid #a00; }
  .btn-details { left: 120px; background: linear-gradient(#e9b630, var(--gold-dark)); border: 1px solid #b07c08; }
</style>
</head>
<body>
  <header class="site-header">
    <div class="brand">
      <span class="brand-mark"></span>
      <span class="brand-name">Lucia's Blue Pantry</span>
    </div>
    <div class="follow" aria-label="Follow me">
      <span class="follow-icon blue-dark"></span>
      <span class="follow-icon blue-light"></span>
      <span class="follow-icon red"></span>
      <span class="follow-icon orange">
        <svg width="24" height="18" viewBox="0 0 24 18"><rect x="1" y="1" width="22" height="16" rx="2" fill="#fff"/><path d="M2 2 L12 10 L22 2" stroke="#f4a324" stroke-width="2" fill="none"/></svg>
      </span>
    </div>
  </header>

  <nav class="main-nav">
    <span class="nav-item" style="left:185px">Home</span>
    <span class="nav-sep" style="left:254px"></span>
    <span class="nav-item" style="left:323px">About</span>
    <span class="nav-sep" style="left:390px"></span>
    <span class="nav-item" style="left:466px">Recipes
      <svg width="14" height="10" viewBox="0 0 14 10" style="margin-left:10px"><path d="M2 2 L7 7 L12 2" stroke="#fff" stroke-width="2.4" fill="none"/></svg></span>
    <span class="nav-sep" style="left:542px"></span>
    <span class="nav-item" style="left:606px">Shop</span>
    <span class="nav-sep" style="left:668px"></span>
    <span class="nav-item" style="left:743px">Events</span>
    <span class="nav-sep" style="left:806px"></span>
    <span class="nav-item" style="left:883px">Travel</span>
    <span class="nav-sep" style="left:945px"></span>
    <span class="nav-item" style="left:1038px">Contact Us</span>
  </nav>

  <section class="hero">
    <div class="hero-photo" role="img" aria-label="Photo of Lucia in a pink oven mitt beside a plate of sushi and prawns"></div>
    <div class="hero-title">Lucia Marbetto in</div>
  </section>

  <h2 class="section-title">Featured Products</h2>

  <article class="product" style="left:111px">
    <div class="product-photo" role="img" aria-label="Tomato sauce in a white gravy boat" style="background:linear-gradient(135deg,#f4f4f6,#e2e2e6 60%,#b33a4a)"></div>
    <h3 class="product-name">Red Tomato Sauce</h3>
    <p class="product-text">You are what you eat. Food you love can tell a lot about your preferen...</p>
    <p class="product-price">$25.00</p>
    <span class="btn btn-buy">Buy</span><span class="btn btn-details">Details</span>
  </article>

  <article class="product" style="left:372px">
    <div class="product-photo" role="img" aria-label="Bowl of iced biscuits" style="background:linear-gradient(135deg,#5fb3d8,#e9d9b0 50%,#d7a8b8)"></div>
    <h3 class="product-name">Biscuiti</h3>
    <p class="product-text">You are what you eat. Food you love can tell a lot about your preferen...</p>
    <p class="product-price">$25.00</p>
    <span class="btn btn-buy">Buy</span><span class="btn btn-details">Details</span>
  </article>

  <article class="product" style="left:632px">
    <div class="product-photo" role="img" aria-label="Plate of fusilli pasta with sauce" style="background:linear-gradient(180deg,#8a2a1e,#b5552e 45%,#f0d27a 80%,#fafafa)"></div>
    <h3 class="product-name">Fusilli Pasta</h3>
    <p class="product-text">You are what you eat. Food you love can tell a lot about your preferen...</p>
    <p class="product-price">$25.00</p>
    <span class="btn btn-buy">Buy</span><span class="btn btn-details">Details</span>
  </article>

  <article class="product" style="left:894px">
    <div class="product-photo" role="img" aria-label="Plate of cannoli" style="background:linear-gradient(135deg,#eee8e2,#c98a4e 50%,#f1ece6)"></div>
    <h3 class="product-name">Cicilian Cannoli</h3>
    <p class="product-text">You are what you eat. Food you love can tell a lot about your preferen...</p>
    <p class="product-price">$25.00</p>
    <span class="btn btn-buy">Buy</span><span class="btn btn-details">Details</span>
  </article>
</body>
</html>
```